Project Title:
Dental Implant Overdenture Flyer (Retirement Village Target)
Objective:
Create a clean, trustworthy, and reassuring flyer aimed at older adults (60–85 years old) who struggle with loose dentures. The goal is to educate them about implant-retained “clip-on” dentures and encourage them to book a consultation.
Tone & Feel:
Warm, caring, non-intimidating
Premium but not “salesy”
Medical but easy to understand
Focus on improving quality of life (confidence, eating, comfort)
Target Audience:
Retirees / pensioners
Existing denture wearers
People frustrated with loose or uncomfortable dentures
Key Message:
“You don’t have to live with loose dentures anymore.”
Design Style:
Clean, minimal, modern
Soft colours (blues, greens, warm neutrals)
Easy-to-read large font
High contrast for older eyes
Avoid clutter
Imagery Suggestions:
Smiling older adults (natural, not stocky/overly staged)
Before/after lifestyle (eating, laughing, socialising)
Simple diagram showing denture clipping onto implants
Avoid graphic surgical images
Layout Suggestions:
A5 or DL flyer
Clear sections with headings
Icons for benefits
Strong call-to-action at bottom
HEADLINE (big and bold)
Tired of Loose Dentures?
Discover Secure “Clip-On” Teeth
🔹 PROBLEM SECTION
Do your dentures:
Slip or move when eating?
Make it hard to chew certain foods?
Feel uncomfortable or loose?
Affect your confidence when speaking or smiling?
You’re not alone — and there is a better solution.
🔹 SOLUTION SECTION
Implant-Retained “Clip-On” Dentures
We can secure your denture using just 2 dental implants, allowing your teeth to:
✔ Stay firmly in place
✔ Improve your ability to eat
✔ Feel more comfortable
✔ Boost your confidence
🔹 SIMPLE EXPLANATION (very important)
Small titanium implants are gently placed in the jaw.
Your denture then clips securely onto them, stopping movement.
🔹 PRICE SECTION (highlight this clearly)
$12,000
Includes:
2 dental implants
A brand new custom overdenture
Does not include sedation or extractions (if needed)
🔹 SEDATION
Sedation is available for comfort.
If you hold a pensioner card, you may receive a significant Vantacor rebate, often resulting in minimal out-of-pocket costs for sedation.
🔹 TRUST / REASSURANCE
Experienced implant clinician
Gentle, patient-focused care
Modern technology and techniques
🔹 CALL TO ACTION (VERY IMPORTANT)
Book a Free Consultation
📞 Call: 08 9351 4276
🌐 Visit: www.bravonclinic.com.au
📍 Located near Tallowmere shopping centre
🔹 OPTIONAL TAGLINE
Eat Better. Feel Better. Smile with Confidence Again.
Please include some photos to illustrate what a clip on denture looks like with two implants.

```html
<!DOCTYPE html>
<html lang="en">
<head>
<meta charset="utf-8">
<title>Clip-On Dentures Flyer</title>
<link rel="stylesheet" href="https://fonts.googleapis.com/css2?family=Alegreya+SC:wght@700;800&family=Oswald:wght@400;500;600&family=Poppins:ital,wght@0,400;0,500;0,600;0,700;0,800;1,500&display=swap">
<style>
:root{
  --stage:#444444;
  --teal:#0b97b1;
  --teal-deep:#0a8aa3;
  --aqua:#1dd3cf;
  --aqua-line:#1ec6c6;
  --mint:#c9f3f3;
  --mist:#e9fbfb;
  --ink:#111518;
  --ink-soft:#1c3b4a;
  --navy:#0d3b4b;
  --white:#ffffff;
}
*{box-sizing:border-box;margin:0;padding:0}
html,body{width:1200px;height:798px;overflow:hidden;background:var(--stage)}
body{position:relative;font-family:"Poppins",sans-serif}
.page{position:absolute;top:64px;width:503px;height:670px;overflow:hidden}
.page--front{left:78px;background:linear-gradient(180deg,var(--mint) 0%,#e4fafa 45%,#f4fdfd 60%,#bff0f0 100%)}
.page--back{left:616px;background:linear-gradient(180deg,#bdf0f0 0%,#e8fbfb 45%,#f4fdfd 70%,#cdf4f4 100%)}
.abs{position:absolute}

/* front */
.brand{left:20px;top:30px;display:flex;align-items:center;gap:8px}
.brand__dot{width:30px;height:30px;border-radius:50%;background:var(--teal)}
.brand__name{font-size:11px;letter-spacing:4px;color:var(--ink-soft);font-weight:500;line-height:1.3}
.brand__sub{font-size:8.5px;letter-spacing:.5px;color:var(--teal);font-weight:600}
.hero-band{left:0;top:79px;width:330px;height:184px;background:var(--teal)}
.hero-blob{left:245px;top:28px;width:258px;height:262px;border-radius:55% 0 0 60% / 50% 0 0 55%;background:var(--aqua)}
.hero-photo{left:290px;top:0;width:213px;height:300px;border-radius:50% 0 0 45% / 40% 0 0 40%;background:linear-gradient(160deg,#bfc9c8 0%,#e6d3c5 40%,#f6f6f4 75%,#eef7f7 100%)}
.headline{left:20px;top:106px;color:var(--white);font-family:"Alegreya SC",serif;font-weight:800;font-size:31px;line-height:38px}
.subhead{left:19px;top:188px;color:var(--white);font-weight:700;font-size:26.5px;line-height:32px}
.problem-title{left:20px;top:281px;font-weight:700;font-size:25px;color:var(--ink)}
.problem-list{left:0;top:328px;width:340px;list-style:none}
.problem-list li{height:27px;padding-left:19px;font-family:"Oswald",sans-serif;font-size:15px;line-height:27px;color:var(--navy)}
.problem-list li:nth-child(odd){background:rgba(200,242,244,.75)}
.problem-list li:nth-child(even){background:rgba(176,234,240,.7)}
.reassure{left:317px;top:297px;width:180px;height:180px;border-radius:50%;background:var(--white);border:4px solid var(--aqua-line);display:flex;align-items:center;justify-content:center;text-align:center}
.reassure p{font-family:"Oswald",sans-serif;font-weight:500;font-size:23px;line-height:34px;color:var(--teal);letter-spacing:-.5px;margin-top:-6px}
.reassure svg{position:absolute;left:22px;top:130px}
.solution-title{left:24px;top:456px;font-weight:700;font-size:30px;line-height:38px;color:var(--ink)}
.solution-title span{display:block;color:var(--teal);margin-left:-7px}
.benefit-box{left:12px;top:566px;width:478px;height:99px;border-radius:16px;background:var(--teal)}
.benefit-pill{left:20px;top:545px;width:446px;height:41px;border-radius:21px;background:var(--aqua);color:var(--white);font-weight:700;font-size:12.5px;line-height:15px;text-align:center;padding-top:6px}
.benefits{left:32px;top:600px;display:grid;grid-template-columns:222px 200px;row-gap:6px}
.benefit{display:flex;align-items:center;gap:6px;color:var(--white);font-size:12.5px;font-weight:500}
.benefit i{width:24px;height:24px;border-radius:50%;border:1.5px dotted var(--white);background:var(--aqua);display:flex;align-items:center;justify-content:center}

/* back */
.denture-photo{left:0;top:0;width:330px;height:225px;background:linear-gradient(170deg,#e7c9b8 0%,#efd6c8 30%,#f3b9c0 50%,#dff6f6 85%,rgba(223,246,246,0) 100%);border-radius:0 0 60px 0}
.explain{left:18px;top:150px;width:180px;font-style:italic;font-weight:500;font-size:12.6px;line-height:23.3px;color:var(--ink-soft);white-space:nowrap}
.price-arc{left:0;top:0}
.price{left:202px;top:24px;width:282px;height:282px;border-radius:50%;background:var(--teal);color:var(--white);text-align:center}
.price__amount{font-weight:800;font-size:47px;line-height:1;margin-top:44px;letter-spacing:-1px}
.price__label{font-weight:700;font-size:15px;margin-top:14px;padding-bottom:2px;border-bottom:1px solid var(--white);width:172px;margin-left:auto;margin-right:auto}
.price__item{font-weight:600;font-size:12.5px;margin-top:8px;display:flex;justify-content:center;align-items:center;gap:4px}
.price__exclude{font-weight:600;font-size:15px;margin-top:12px;border-bottom:1px solid var(--white);width:172px;margin-left:auto;margin-right:auto;padding-bottom:1px}
.price__note{font-weight:500;font-size:12.5px;line-height:15px;margin-top:4px}
.sedation-pill{left:0;top:279px;width:221px;height:52px;border-radius:0 26px 26px 0;background:var(--aqua);color:var(--white);font-weight:600;font-size:16.5px;line-height:21px;padding:6px 0 0 21px}
.rebate{left:242px;top:293px;width:202px;height:242px;background:linear-gradient(180deg,var(--teal) 0%,#17b9c4 50%,var(--aqua) 100%);color:var(--white);text-align:center;font-weight:500;font-size:13.3px;line-height:28px;padding-top:48px}
.trust{left:17px;top:351px;list-style:none}
.trust li{display:flex;align-items:center;gap:7px;height:51px;font-weight:500;font-size:14px;line-height:16.5px;color:var(--ink)}
.trust i{width:44px;height:44px;border-radius:50%;border:1.5px dotted var(--teal);display:flex;align-items:center;justify-content:center}
.trust i b{width:38px;height:38px;border-radius:50%;background:var(--teal);display:block}
.trust li:nth-child(2) i b{background:var(--aqua)}
.model-art{left:85px;top:455px;width:155px;height:80px;border-radius:20px 20px 0 0;background:linear-gradient(180deg,rgba(243,205,210,.35),rgba(243,220,224,.55))}
.cta-band{left:0;top:533px;width:503px;height:54px;background:#b9ecef}
.cta{left:29px;top:533px;width:446px;height:54px;border-radius:27px;background:var(--teal);border:2px solid var(--white);color:var(--white);font-family:"Oswald",sans-serif;font-weight:600;font-size:33px;line-height:48px;text-align:center;letter-spacing:-.3px}
.contacts{left:0;top:592px;width:503px}
.contact{position:absolute;top:0;display:flex;flex-direction:column;align-items:center;gap:5px;font-weight:500;font-size:10.5px;color:var(--ink);white-space:nowrap}
.contact i{width:21px;height:21px;border-radius:50%;border:1.5px solid var(--aqua-line);background:var(--white);display:flex;align-items:center;justify-content:center}
.tagline{left:22px;top:640px;width:459px;height:25px;border-radius:13px;background:var(--aqua);color:var(--white);font-size:12.5px;line-height:25px;text-align:center}
</style>
</head>
<body>

<section class="page page--front">
  <div class="abs hero-blob"></div>
  <div class="abs hero-band"></div>
  <div class="abs hero-photo" role="img" aria-label="Photo of a smiling older woman pointing at her teeth"></div>

  <div class="abs brand">
    <span class="brand__dot"></span>
    <div>
      <div class="brand__name">BRAVON CLINIC</div>
      <div class="brand__sub">DENTAL SURGERY</div>
    </div>
  </div>

  <h1 class="abs headline">Tired of Loose<br>Dentures?</h1>
  <h2 class="abs subhead">DISCOVER SECURE<br>“CLIP-ON” TEETH</h2>

  <h3 class="abs problem-title">DO YOUR DENTURES:</h3>
  <ul class="abs problem-list">
    <li>Slip or move when eating?</li>
    <li>Make it hard to chew certain foods?</li>
    <li>Feel uncomfortable or loose?</li>
    <li>Affect your confidence when speaking or smiling?</li>
  </ul>

  <div class="abs reassure">
    <p>YOU’RE NOT<br>ALONE AND<br>THERE IS A BETTER<br>SOLUTION.</p>
    <svg width="128" height="30" viewBox="0 0 128 30"><path d="M4 4 Q64 44 124 4" fill="none" stroke="var(--teal)" stroke-width="1.5" stroke-dasharray="2 1.5"/><circle cx="4" cy="4" r="3.5" fill="var(--teal)"/><circle cx="124" cy="4" r="3.5" fill="var(--teal)"/></svg>
  </div>

  <h2 class="abs solution-title">IMPLANT-RETAINED<span>“CLIP-ON” DENTURES</span></h2>

  <div class="abs benefit-box"></div>
  <p class="abs benefit-pill">We can secure your denture using just 2 dental implants,<br>allowing your teeth to:</p>
  <div class="abs benefits">
    <div class="benefit"><i><svg width="12" height="12" viewBox="0 0 12 12"><path d="M2 6l3 3 5-6" fill="none" stroke="#fff" stroke-width="1.6"/></svg></i>Stay firmly in place</div>
    <div class="benefit"><i><svg width="12" height="12" viewBox="0 0 12 12"><path d="M2 6l3 3 5-6" fill="none" stroke="#fff" stroke-width="1.6"/></svg></i>Feel more comfortable</div>
    <div class="benefit"><i><svg width="12" height="12" viewBox="0 0 12 12"><path d="M2 6l3 3 5-6" fill="none" stroke="#fff" stroke-width="1.6"/></svg></i>Improve your ability to eat</div>
    <div class="benefit"><i><svg width="12" height="12" viewBox="0 0 12 12"><path d="M2 6l3 3 5-6" fill="none" stroke="#fff" stroke-width="1.6"/></svg></i>Boost your confidence</div>
  </div>
</section>

<section class="page page--back">
  <div class="abs denture-photo" role="img" aria-label="Photo of hands holding a full clip-on denture set"></div>

  <p class="abs explain">Small titanium implants are<br>gently placed in the jaw.<br>Your denture then clips<br>securely onto them,<br>stopping movement.</p>

  <div class="abs sedation-pill">Sedation is available<br>for comfort.</div>

  <div class="abs rebate">If you hold a pensioner<br>card, you may receive<br>a significant Vantacor<br>rebate, often resulting<br>in minimal<br>out-of-pocket costs for<br>sedation.</div>

  <svg class="abs price-arc" width="503" height="340" viewBox="0 0 503 340">
    <path d="M193 222 A151 151 0 0 0 493 222" fill="none" stroke="var(--aqua-line)" stroke-width="4"/>
    <circle cx="193" cy="222" r="6" fill="var(--teal)"/>
    <circle cx="493" cy="222" r="6" fill="var(--teal)"/>
  </svg>

  <div class="abs price">
    <div class="price__amount">$12,000</div>
    <div class="price__label">Includes:</div>
    <div class="price__item"><svg width="14" height="14" viewBox="0 0 14 14"><circle cx="7" cy="7" r="6" fill="none" stroke="#fff" stroke-width="1.3"/><path d="M4 7l2 2 4-5" fill="none" stroke="#fff" stroke-width="1.5"/></svg>2 dental implants</div>
    <div class="price__item"><svg width="14" height="14" viewBox="0 0 14 14"><circle cx="7" cy="7" r="6" fill="none" stroke="#fff" stroke-width="1.3"/><path d="M4 7l2 2 4-5" fill="none" stroke="#fff" stroke-width="1.5"/></svg>A brand new custom overdenture</div>
    <div class="price__exclude">Does not include</div>
    <div class="price__note">sedation or<br>extractions (if needed)</div>
  </div>

  <div class="abs model-art" role="img" aria-label="Illustration of a denture model clipping onto two implants beside a cartoon tooth"></div>

  <ul class="abs trust">
    <li><i><b></b></i>Experienced implant<br>clinician</li>
    <li><i><b></b></i>Gentle, patient-focused<br>care</li>
    <li><i><b></b></i>Modern technology<br>and techniques</li>
  </ul>

  <div class="abs cta-band"></div>
  <div class="abs cta">BOOK A FREE CONSULTATION</div>

  <div class="abs contacts">
    <div class="contact" style="left:18px"><i><svg width="11" height="11" viewBox="0 0 24 24"><path d="M6.6 10.8a15 15 0 0 0 6.6 6.6l2.2-2.2c.3-.3.7-.4 1-.2 1.1.4 2.3.6 3.6.6.6 0 1 .4 1 1V20c0 .6-.4 1-1 1A17 17 0 0 1 3 4c0-.6.4-1 1-1h3.5c.6 0 1 .4 1 1 0 1.3.2 2.5.6 3.6.1.3 0 .7-.2 1z" fill="var(--teal)"/></svg></i>08 9351 4276</div>
    <div class="contact" style="left:113px"><i><svg width="11" height="11" viewBox="0 0 24 24"><circle cx="12" cy="12" r="10" fill="none" stroke="var(--teal)" stroke-width="2"/><path d="M2 12h20M12 2c3 3 3 17 0 20M12 2c-3 3-3 17 0 20" fill="none" stroke="var(--teal)" stroke-width="1.6"/></svg></i>www.bravonclinic.com.au</div>
    <div class="contact" style="left:272px"><i><svg width="10" height="12" viewBox="0 0 20 24"><path d="M10 1a8 8 0 0 0-8 8c0 6 8 14 8 14s8-8 8-14a8 8 0 0 0-8-8z" fill="var(--teal)"/><circle cx="10" cy="9" r="3" fill="#fff"/></svg></i>Located near Tallowmere shopping centre</div>
  </div>

  <div class="abs tagline">Eat Better. Feel Better. Smile with Confidence Again.</div>
</section>

</body>
</html>
```